Thoroughbred Racing Partnership needs web design

Crest of Fortune Partners is a management group who buys horses and races them on both the West and East coasts. The premise of the business is for an investment as little as $500, anyone can be a partner and own a percentage of a horse(s). This is a low cost way of getting involved in the exciting sport of Thoroughbred Racing, without shouldering the heavy financial responsibility. Our target market is mostly males 40+ but we want to include all target markets. We are looking for something very clean and professional, we want to give an image of success. Nothing overly "artsy." I have included the logo in which you can incorporate in the site. Also, the logo colors will be the colors of our "silks." The silks are what the jockey wears and will be an important marketing tool for COF. We would like a very prominent picture of a racehorse somewhere on the homepage, we want to make it clear that is a website for Horseracing partnerships.

On the top of the site, it should say "Crest of Fortune" (on the top)
and below that "Thoroughbred Racing Partnerships." (below that)

The main sections, which should be across the top are:

Home
About Us
Ownership
Stable Roster
News
Contact us

Some of these will have drop down menus.

An example of a competitor website that we like is: www.harlowfieldeq.example
An example of a competitor website that we don't like is: www.gallopvane.example
Updates

Project Deadline Extended
Reason: We have a Board of Directors meeting on the 22nd and we will be making a decision on that day. I'm giving an extension so that all designers are able to submit their designs by the 22nd. Thank you!

Target Market(s)

40+ males

Industry/Entity Type

Business

Requirements
Must have
• our logo must be on the site. We would like at least one bold image of a thoroughbred horse in action. The picture is going to tell the story so it needs to be very eye-catching.

Our slogan should also be included on the website, "Experience the thrill of owning a Racehorse."
Should not have
• cartoons, artsy pictures, pictures of Steeplechase horses or "jumpers." This partnership is for racehorses only, there is not jumping involved with the horses.

```html
<!DOCTYPE html>
<html lang="en">
<head>
<meta charset="utf-8">
<title>Crest of Fortune Partners – Thoroughbred Racing Partnerships</title>
<link href="https://fonts.googleapis.com/css2?family=Oswald:wght@500&family=Roboto:wght@400;500&display=swap" rel="stylesheet">
<style>
:root{
  --ink:#2b2b2b;
  --navy:#0f3f73;
  --blue:#1f6195;
  --blue-dark:#0d3a6a;
  --band:#1c5e92;
  --link:#1d6aa5;
  --text:#555;
  --muted:#888;
  --paper:#fff;
  --footer-text:#d8d8d8;
}
*{margin:0;padding:0;box-sizing:border-box}
html,body{width:960px;height:1200px;overflow:hidden}
body{position:relative;background:var(--paper);font-family:"Roboto",sans-serif;color:var(--text)}
.abs{position:absolute}
.topbar{left:0;top:0;width:960px;height:97px;background:var(--ink)}
.toplinks{right:104px;top:8px;font-size:10px;font-weight:500;color:#fff;letter-spacing:.3px}
.toplinks span{margin:0 7px;color:#aaa}
.hero{left:0;top:97px;width:960px;height:436px;background:linear-gradient(160deg,#7fa4cf 0%,#b7cbe0 35%,#6d4a35 60%,#3b2a22 100%)}
.header{left:104px;top:29px;width:752px;height:117px;background:linear-gradient(#fff,#eef0f2);border:1px solid #ddd;border-radius:3px;box-shadow:0 2px 6px rgba(0,0,0,.3)}
.brand{left:16px;top:40px;display:flex;align-items:center;gap:8px;font-size:24px;font-weight:500;color:var(--navy)}
.brand i{width:18px;height:18px;border-radius:50%;background:var(--navy);display:block}
.site-title{right:56px;top:16px;font-size:21px;font-weight:500;color:var(--navy);letter-spacing:.5px}
.site-sub{right:12px;top:46px;font-size:16px;color:#444;letter-spacing:.4px}
.nav{left:231px;top:76px;width:511px;height:35px;background:linear-gradient(#2d72a8,#1b5687);display:flex;border-radius:2px;font-size:11px;color:#fff}
.nav a{color:#fff;text-decoration:none;line-height:35px;padding:0 15px}
.nav a.current{background:var(--blue-dark)}
.slogan{left:104px;top:318px;font-family:"Oswald",sans-serif;font-weight:500;font-size:41px;line-height:42px;color:#fff;text-shadow:0 2px 4px rgba(0,0,0,.5);letter-spacing:-.5px}
.dots{left:104px;top:495px;display:flex;gap:4px}
.dots i{width:12px;height:12px;border-radius:50%;background:#2e6d9b;display:block}
.dots i:first-child{background:#3b8bc4}
.login{left:0;top:533px;width:960px;height:54px;background:var(--band)}
.login-label{left:104px;top:552px;font-size:15px;font-weight:500;color:#fff;letter-spacing:.3px}
.field{top:547px;height:26px;background:#f3f3f3;border-radius:2px;font-size:11px;color:#999;padding-left:12px;line-height:26px}
.btn{left:513px;top:547px;width:65px;height:26px;background:#2f2f2f;border-radius:3px;color:#fff;font-size:11px;font-weight:500;text-align:center;line-height:26px}
.follow{left:666px;top:533px;width:190px;height:54px;background:var(--blue-dark)}
.follow-label{left:680px;top:554px;font-size:13px;font-weight:500;color:#fff}
.social{top:549px;width:23px;height:23px;border-radius:3px}
.welcome-img{left:104px;top:615px;width:238px;height:151px;background:linear-gradient(135deg,#6b8a6a,#9c5a35 55%,#c77d9a)}
h2{font-weight:400;color:var(--navy);font-size:19px;letter-spacing:.3px}
.welcome-title{left:360px;top:613px}
.welcome-text{left:360px;top:640px;width:500px;font-size:10.4px;line-height:18.4px;letter-spacing:.2px}
.more{left:359px;top:752px;font-size:10px;font-weight:500;color:var(--link)}
.rule{left:104px;top:784px;width:752px;height:1px;background:#999}
.news-title{left:105px;top:798px}
.news-item{left:105px;width:330px;border-bottom:1px dashed #aaa;padding-bottom:7px}
.news-item p{font-size:11px;line-height:16px;color:var(--link);font-weight:500;letter-spacing:.2px}
.news-item time{display:block;font-size:10.4px;color:#666;margin-top:6px}
.news-item.last{border:none}
.video-title{left:488px;top:798px}
.video{left:488px;top:831px;width:368px;height:183px;background:#ccc;padding:3px}
.video-still{width:100%;height:100%;background:linear-gradient(135deg,#3d4a3a,#b06a3e 55%,#d98a8a)}
.play{left:158px;top:70px}
.footer{left:0;top:1037px;width:960px;height:163px;background:var(--ink)}
.disclaimer{left:104px;top:1055px;width:200px;font-size:10.4px;line-height:16px;color:var(--footer-text)}
.foot-brand{left:104px;top:1110px;display:flex;align-items:center;gap:6px;font-size:17px;font-weight:500;color:#fff}
.foot-brand i{width:12px;height:12px;border-radius:50%;background:#fff;display:block}
.copy{left:104px;top:1155px;font-size:10.4px;line-height:16px;color:var(--muted)}
.col h3{font-weight:400;font-size:13.5px;color:#fff;margin-bottom:4px}
.col{top:1054px;font-size:10.4px;line-height:17.6px;color:#bbb;letter-spacing:.3px}
.col .co{color:#3a8fd0;font-size:11px}
.col .val{color:#fff}
.col .gap{margin-top:5px}
</style>
</head>
<body>
<div class="abs topbar"></div>
<div class="abs toplinks">LOGIN<span>|</span>SHARE THIS PAGE</div>

<div class="abs hero" role="img" aria-label="Photo of two thoroughbred racehorses at full gallop with jockeys in purple and yellow silks under a blue sky"></div>

<header class="abs header">
  <div class="abs brand"><i></i>COF Partners</div>
  <div class="abs site-title">CREST OF FORTUNE</div>
  <div class="abs site-sub">Thoroughbred Racing Partnerships</div>
  <nav class="abs nav">
    <a class="current">HOME</a><a>ABOUT US</a><a>OWNERSHIP</a><a>STABLE ROSTER</a><a>NEWS</a><a>CONTACT US</a>
  </nav>
</header>

<div class="abs slogan">EXPERIENCE THE THRILL OF<br>OWNING A RACEHORSE</div>
<div class="abs dots"><i></i><i></i><i></i><i></i></div>

<section class="abs login"></section>
<div class="abs login-label">USER LOGIN:</div>
<div class="abs field" style="left:202px;width:150px">USERNAME</div>
<div class="abs field" style="left:355px;width:150px">PASSWORD</div>
<div class="abs btn">LOG IN</div>
<div class="abs follow"></div>
<div class="abs follow-label">FOLLOW US:</div>
<div class="abs social" style="left:763px;background:#3b5a98" aria-label="Social profile"></div>
<div class="abs social" style="left:793px;background:#41b7e3" aria-label="Social profile"></div>
<div class="abs social" style="left:823px;background:#c4302b" aria-label="Video channel"></div>

<div class="abs welcome-img" role="img" aria-label="Photo of a chestnut racehorse with a jockey in red silks racing past flowers"></div>
<h2 class="abs welcome-title">Welcome to Our WebSite</h2>
<p class="abs welcome-text">Aliquam molestie, mi et imperdiet euismod, dui purus auctor tellus, et interdum lacus lectus et ante. Sed accumsan sollicitudin sapien, sit amet adipiscing turpis gravida ac. In congue, neque ac lobortis volutpat, libero mauris varius mi, vitae suscipit ipsum ligula vitae risus. Duis aliquam nibh a dui iaculis viverra id a velit. Vivamus egestas risus in magna varius commodo. Sed semper viverra egestas. Etiam pretium porttitor lectus, vel ornare neque porta volutpat.</p>
<div class="abs more">READ MORE&gt;&gt;</div>
<div class="abs rule"></div>

<h2 class="abs news-title">Stable News</h2>
<article class="abs news-item" style="top:828px"><p>Aliquam molestie, mi et imperdiet euismod, dui purus auctor tellus, et interdum lacus lectus et ante.</p><time>October 25, 2013</time></article>
<article class="abs news-item" style="top:895px"><p>Aliquam molestie, mi et imperdiet euismod, dui purus auctor tellus, et interdum lacus lectus et ante.</p><time>October 25, 2013</time></article>
<article class="abs news-item last" style="top:961px"><p>Aliquam molestie, mi et imperdiet euismod, dui purus auctor tellus, et interdum lacus lectus et ante.</p><time>October 25, 2013</time></article>

<h2 class="abs video-title">Watch a Video</h2>
<div class="abs video">
  <div class="video-still" role="img" aria-label="Video still of a racehorse with number 8 saddle cloth and a jockey in blue and pink silks"></div>
  <svg class="abs play" width="52" height="38" viewBox="0 0 52 38"><rect width="52" height="38" rx="6" fill="#d0231f"/><path d="M20 11 L34 19 L20 27Z" fill="#fff"/></svg>
</div>

<footer class="abs footer"></footer>
<p class="abs disclaimer">We are not affiliated with the Northgate Riding Academy.</p>
<div class="abs foot-brand"><i></i>COF Partners</div>
<p class="abs copy">Copyright © 2013 All rights reserved.<br>Site Map · Contact Us</p>

<div class="abs col" style="left:360px"><h3>Quick Links</h3>Home<br>About Us<br>Ownership<br>Stable Roster<br>News<br>Contact us</div>
<div class="abs col" style="left:510px"><h3>Company Headquarters</h3><span class="co">COF Partners</span><br>412 Fenwick<br>Lane,Aldermoor, AM7 3KD<div class="gap">Phone: <span class="val">+1 800 555 0142</span></div><div class="gap">Email : <span class="val">info@cofpartners.example</span></div></div>
<div class="abs col" style="left:706px"><h3>Regional Offices</h3><span class="co">COF Partners</span><br>412 Fenwick<br>Lane,Aldermoor, AM7 3KD<div class="gap">Phone: <span class="val">+1 800 555 0142</span></div><div class="gap">Email : <span class="val">info@cofpartners.example</span></div></div>
</body>
</html>
```